Mortgage and Asset Finance Broker Needs a Wordpress Website Design

I need a modern looking Wordpress website to showcase my service as a mortgage and asset broker. I have a company and we work with various lenders to arrange mortgages, as well as commercial lending and business asset finance. The website needs to look professional, be easy to navigate and capture leads. SEO is obviously very important to me. It really needs to be something that shows trust and professioanlism.
Updates

On the home page I will need to have some boxes for Home Loans, Refinancing, Business (and Agriculture) Loans etc. I'd like a carousel in the middle which shows our lenders (so that can have the banks logos added).

It needs to be easy top navigate and showcase all we do - Home Loans, Refinancing, Commercial Loans, Car Loans, Asset Finance etc.

There are plenty of companies on the internet that do this.

There is some good information here https://lendquill.example.au/mortgage-broker-homepage/

I need to make sure that editing the website is easy (I think Wordpress has something that allows that).

Also we are very much an Australian business so that is something to advertise.

Industry/Entity Type

Mortgage and Finance Broker

Coding

Coded - Design and coding required

Number of Pages Required

5+ page

Requirements
Must have
• Easy to navigate professional feel. Must be responsive and mobile friendly.
Nice to have
• Homepage with links to inner pages. Contact buttons.

```html
<!DOCTYPE html>
<html lang="en">
<head>
<meta charset="utf-8">
<title>Northvale Finance – Mortgage &amp; Asset Finance Broker</title>
<link rel="stylesheet" href="https://fonts.googleapis.com/css2?family=Poppins:wght@400;500;600;700;800&display=swap">
<style>
:root{
  --blue:#1c5fae;
  --blue-dark:#12467f;
  --orange:#f39a2b;
  --ink:#1d2430;
  --muted:#6b7380;
  --line:#e4e7ec;
  --white:#ffffff;
  --footer:#232427;
}
*{box-sizing:border-box;margin:0;padding:0}
html,body{width:1200px;height:4248px;overflow:hidden}
body{font-family:"Poppins",sans-serif;color:var(--ink);background:var(--white);position:relative}
.abs{position:absolute}
a{color:inherit;text-decoration:none}

/* top bar */
.topbar{left:0;top:0;width:1200px;height:40px;background:var(--blue);color:var(--white);font-size:12px;display:flex;align-items:center;padding:0 48px;gap:40px}
.topbar .item{display:flex;align-items:center;gap:8px}
.topbar .social{margin-left:auto;display:flex;gap:12px}
.topbar .social span{width:14px;height:14px;border-radius:50%;background:var(--white);opacity:.9;display:block}

/* header */
.header{left:0;top:40px;width:1200px;height:96px;background:var(--white);display:flex;align-items:center;padding:0 48px}
.brand{display:flex;align-items:center;gap:10px;font-size:26px;font-weight:700;color:var(--blue)}
.brand .dot{width:14px;height:14px;background:var(--orange)}
.nav{display:flex;gap:44px;margin-left:90px;font-size:14px;font-weight:600}
.phone-pill{margin-left:auto;background:var(--orange);color:var(--white);font-weight:600;font-size:14px;padding:9px 28px;border-radius:22px}

/* hero */
.hero{left:0;top:136px;width:1200px;height:624px;background:linear-gradient(90deg,#3b4350 0%,#6c7580 45%,#c9c4bb 75%,#ece6dc 100%)}
.hero-copy{left:80px;top:290px;width:560px;color:var(--white)}
.hero-copy h1{font-size:50px;line-height:1.18;font-weight:700}
.hero-copy p{margin-top:18px;font-size:15px;line-height:1.6;opacity:.92}
.btn{display:inline-block;font-weight:600;font-size:13px;padding:13px 30px;border-radius:24px}
.btn-orange{background:var(--orange);color:var(--white)}
.btn-outline{border:2px solid var(--white);color:var(--white);padding:11px 28px}
.btn-row{display:flex;gap:14px;margin-top:26px}

/* features */
.features{left:160px;top:640px;width:880px;height:232px;background:var(--white);box-shadow:0 10px 30px rgba(0,0,0,.12);display:flex;padding:46px 40px;gap:40px}
.feature{flex:1}
.feature h3{font-size:17px;font-weight:600;margin-top:14px;line-height:1.3}
.feature p{font-size:13px;color:var(--muted);margin-top:8px;line-height:1.6}

/* about */
.about-photo{left:80px;top:1048px;width:480px;height:400px;background:linear-gradient(135deg,#e2d6c8 0%,#b9a08a 55%,#8f7764 100%)}
.about-copy{left:640px;top:1100px;width:460px}
.section-title{font-size:32px;font-weight:700;color:var(--ink)}
.underline{width:60px;height:4px;background:var(--blue);margin-top:10px}
.about-copy p{font-size:12.5px;color:var(--muted);line-height:1.75;margin-top:18px}
.about-copy .btn{margin-top:22px;padding:10px 26px;font-size:12px}

/* what we do */
.services-band{left:0;top:1580px;width:1200px;height:700px;background:var(--blue)}
.services-title{left:80px;top:1655px;color:var(--white)}
.services-title .underline{background:var(--orange)}
.services-intro{left:400px;top:1668px;width:520px;color:var(--white);font-size:13px;line-height:1.65;opacity:.92}
.view-all{left:968px;top:1672px;background:var(--orange);color:var(--white);font-weight:600;font-size:13px;padding:11px 34px;border-radius:24px}
.card{top:1808px;width:248px;height:412px;background:var(--white);box-shadow:0 8px 24px rgba(0,0,0,.12)}
.card .photo{width:248px;height:172px}
.card .body{padding:22px 20px}
.card h3{font-size:17px;font-weight:600}
.card ul{list-style:none;margin-top:14px}
.card li{font-size:12px;color:var(--muted);display:flex;align-items:center;gap:8px;padding:7px 0;border-bottom:1px solid var(--line)}
.card li::before{content:"";width:6px;height:6px;border-radius:50%;background:var(--orange);flex:none}
.card .btn{margin-top:16px;padding:7px 18px;font-size:10px}

/* lenders */
.lenders-title{left:0;top:2350px;width:1200px;text-align:center;font-size:30px;font-weight:700}
.lenders{left:110px;top:2462px;width:980px;display:flex;justify-content:space-between;align-items:center;font-size:27px;font-weight:700;color:#111}

/* contact */
.contact{left:0;top:2632px;width:1200px;height:580px;background:linear-gradient(135deg,#f5a33a,#ef9125)}
.contact-title{left:172px;top:2732px;color:var(--white);font-size:30px;font-weight:700}
.field{background:var(--white);height:52px;font-size:13px;color:#9aa0a8;padding:0 18px;display:flex;align-items:center}
.btn-blue{background:var(--blue);color:var(--white);padding:11px 22px;font-size:12px;border-radius:22px}

/* testimonials */
.testi-title{left:0;top:3310px;width:1200px;text-align:center;font-size:30px;font-weight:700}
.testi{top:3420px;width:280px;height:330px;background:var(--white);box-shadow:0 8px 26px rgba(0,0,0,.12);padding:38px 24px 24px;overflow:hidden}
.testi .avatar{width:70px;height:70px;border-radius:50%;background:linear-gradient(135deg,#c79f7e,#7e5c48)}
.testi .quote{position:absolute;right:0;top:0;width:96px;height:96px}
.testi h4{font-size:16px;font-weight:600;margin-top:18px}
.stars{display:flex;gap:3px;margin-top:6px}
.testi p{font-size:12px;color:var(--muted);line-height:1.65;margin-top:12px}
.arrow{top:3560px}

/* footer */
.footer{left:0;top:3848px;width:1200px;height:352px;background:var(--footer)}
.footer-about{left:100px;top:3920px;width:340px;color:var(--white)}
.footer-about .brand{color:var(--white)}
.footer-about p{font-size:14px;line-height:1.7;margin-top:18px;opacity:.85}
.footer-about .social{display:flex;gap:12px;margin-top:22px}
.footer-about .social span{width:28px;height:28px;border-radius:50%;background:rgba(255,255,255,.18);display:block}
.footer-col{color:var(--white)}
.footer-col h4{font-size:16px;font-weight:600;letter-spacing:.5px}
.footer-col ul{list-style:none;margin-top:14px}
.footer-col li{font-size:14px;padding:6px 0;display:flex;align-items:center;gap:12px}
.footer-col li::before{content:"";width:7px;height:7px;border-radius:50%;background:var(--orange)}
.footer-links{left:520px;top:3920px}
.footer-contact{left:820px;top:3920px}
.footer-contact .row{display:flex;align-items:center;gap:14px;font-size:14px;margin-top:18px}
.copyright{left:0;top:4200px;width:1200px;height:48px;background:var(--blue);color:var(--white);font-size:12px;display:flex;align-items:center;padding-left:100px}
</style>
</head>
<body>

<div class="abs topbar">
  <div class="item">
    <svg width="14" height="14" viewBox="0 0 24 24" fill="none" stroke="#fff" stroke-width="2"><rect x="3" y="5" width="18" height="14" rx="2"/><path d="M3 7l9 6 9-6"/></svg>
    hello@northvale.example
  </div>
  <div class="item">
    <svg width="14" height="14" viewBox="0 0 24 24" fill="#fff"><path d="M12 2a7 7 0 0 0-7 7c0 5 7 13 7 13s7-8 7-13a7 7 0 0 0-7-7zm0 9.5A2.5 2.5 0 1 1 12 6.5a2.5 2.5 0 0 1 0 5z"/></svg>
    18 Wattle St, Parramatta
  </div>
  <div class="social"><span></span><span></span><span></span></div>
</div>

<header class="abs header">
  <div class="brand"><span class="dot"></span>Northvale Finance</div>
  <nav class="nav">
    <a href="#">HOME</a><a href="#">ABOUT</a><a href="#">SERVICES</a><a href="#">NEWS</a><a href="#">CONTACT</a>
  </nav>
  <a class="phone-pill" href="#">(02) 5550 1842</a>
</header>

<section class="abs hero" role="img" aria-label="Photo of a happy family at home, parent lifting a child"></section>
<div class="abs hero-copy">
  <h1>Unlocking Doors<br>&amp; Realizing Dreams</h1>
  <p>Lorem ipsum dolor sit amet, consectetur adipiscing elit. Ut elit tellus, luctus nec ullamcorper mattis, pulvinar dapibus leo.</p>
  <div class="btn-row">
    <a class="btn btn-orange" href="#">GET A QUOTE</a>
    <a class="btn btn-outline" href="#">LEARN MORE</a>
  </div>
</div>

<section class="abs features">
  <div class="feature">
    <svg width="44" height="44" viewBox="0 0 44 44" fill="none" stroke="#1c5fae" stroke-width="2"><circle cx="22" cy="22" r="18"/><path d="M22 12v20M27 16h-7a3 3 0 0 0 0 6h4a3 3 0 0 1 0 6h-7"/></svg>
    <h3>Competitive Interest Rates</h3>
    <p>Lorem ipsum dolor sit amet, consectetur adipiscing elit.</p>
  </div>
  <div class="feature">
    <svg width="44" height="44" viewBox="0 0 44 44" fill="none" stroke="#1c5fae" stroke-width="2"><path d="M6 38h32M10 38V20M18 38V14M26 38V22M34 38V10"/><path d="M8 14l10-8 8 6 10-6"/></svg>
    <h3>Flexible Loan Options</h3>
    <p>Lorem ipsum dolor sit amet, consectetur adipiscing elit.</p>
  </div>
  <div class="feature">
    <svg width="44" height="44" viewBox="0 0 44 44" fill="none" stroke="#1c5fae" stroke-width="2"><circle cx="22" cy="22" r="16"/><path d="M14 22l6 6 10-12"/></svg>
    <h3>Efficient &amp; Efficient Process</h3>
    <p>Lorem ipsum dolor sit amet, consectetur adipiscing elit.</p>
  </div>
</section>

<div class="abs about-photo" role="img" aria-label="Collage of photos showing families and couples with their new homes"></div>
<section class="abs about-copy">
  <h2 class="section-title">ABOUT US</h2>
  <div class="underline"></div>
  <p>We help clients across Australia find the right home loan, with clear advice and lenders who suit their goals. Our team compares options so you can borrow with confidence and save time and money.</p>
  <p>We look beyond the rate to the features, fees and flexibility of each loan. Our goal is to give you a simple path from first enquiry to settlement, with honest guidance at every single step.</p>
  <a class="btn btn-orange" href="#">GET A QUOTE</a>
</section>

<section class="abs services-band"></section>
<div class="abs services-title">
  <h2 class="section-title" style="color:#fff">WHAT WE DO</h2>
  <div class="underline"></div>
</div>
<p class="abs services-intro">We compare loans from a wide panel of lenders to find the one that fits you, whether you are buying, refinancing or growing a business.</p>
<a class="abs view-all" href="#">VIEW ALL</a>

<article class="abs card" style="left:80px">
  <div class="photo" role="img" aria-label="Photo of a family with a miniature house" style="background:linear-gradient(135deg,#d7c6b3,#8a6f58)"></div>
  <div class="body">
    <h3>Home Loans</h3>
    <ul><li>Lorem ipsum dolor sit amet</li><li>Consectetur adipiscing elit</li><li>Nullam aliquet dolor eu mattis</li><li>Sollicitudin eleifend nulla</li></ul>
    <a class="btn btn-orange" href="#">LEARN MORE</a>
  </div>
</article>
<article class="abs card" style="left:344px">
  <div class="photo" role="img" aria-label="Photo of a couple reviewing documents with an adviser" style="background:linear-gradient(135deg,#6b5346,#2f2a28)"></div>
  <div class="body">
    <h3>Refinancing Option</h3>
    <ul><li>Lorem ipsum dolor sit amet</li><li>Consectetur adipiscing elit</li><li>Nullam aliquet dolor eu mattis</li><li>Sollicitudin eleifend nulla</li></ul>
    <a class="btn btn-orange" href="#">LEARN MORE</a>
  </div>
</article>
<article class="abs card" style="left:608px">
  <div class="photo" role="img" aria-label="Photo of a business meeting over paperwork" style="background:linear-gradient(135deg,#c8c2ba,#7d776f)"></div>
  <div class="body">
    <h3>Commercial Loans</h3>
    <ul><li>Lorem ipsum dolor sit amet</li><li>Consectetur adipiscing elit</li><li>Nullam aliquet dolor eu mattis</li><li>Sollicitudin eleifend nulla</li></ul>
    <a class="btn btn-orange" href="#">LEARN MORE</a>
  </div>
</article>
<article class="abs card" style="left:872px">
  <div class="photo" role="img" aria-label="Photo of a toy car with a calculator" style="background:linear-gradient(135deg,#e2e4e8,#c44a3c)"></div>
  <div class="body">
    <h3>Car Loans</h3>
    <ul><li>Lorem ipsum dolor sit amet</li><li>Consectetur adipiscing elit</li><li>Nullam aliquet dolor eu mattis</li><li>Sollicitudin eleifend nulla</li></ul>
    <a class="btn btn-orange" href="#">LEARN MORE</a>
  </div>
</article>

<h2 class="abs lenders-title">OUR LENDERS</h2>
<div class="abs lenders">
  <span>Tallow</span><span>Brookfin</span><span>Brookfin</span><span>Quayside</span><span>Ardent</span><span>Pinecrest</span>
</div>

<section class="abs contact" role="img" aria-label="Faint photo of a family at home behind an orange overlay"></section>
<h2 class="abs contact-title">GET IN TOUCH</h2>
<div class="abs field" style="left:172px;top:2840px;width:268px">Name</div>
<div class="abs field" style="left:460px;top:2840px;width:260px">Email</div>
<div class="abs field" style="left:740px;top:2840px;width:260px">Phone</div>
<div class="abs field" style="left:172px;top:2920px;width:828px;height:140px;align-items:flex-start;padding-top:16px">Message</div>
<a class="abs btn btn-blue" style="left:172px;top:3100px" href="#">GET A QUOTE</a>

<h2 class="abs testi-title">TESTIMONIALS</h2>
<svg class="abs arrow" style="left:52px" width="28" height="40" viewBox="0 0 28 40"><path d="M20 6L8 20l12 14" fill="none" stroke="#1c5fae" stroke-width="4"/></svg>
<svg class="abs arrow" style="left:1120px" width="28" height="40" viewBox="0 0 28 40"><path d="M8 6l12 14L8 34" fill="none" stroke="#1c5fae" stroke-width="4"/></svg>

<article class="abs testi" style="left:140px">
  <svg class="quote" viewBox="0 0 96 96"><path d="M0 0h96v96A96 96 0 0 1 0 0z" fill="#1c5fae"/><text x="52" y="52" fill="#fff" font-family="Poppins,sans-serif" font-size="44" font-weight="700">“</text></svg>
  <div class="avatar" role="img" aria-label="Client portrait"></div>
  <h4>Liam Carter</h4>
  <div class="stars"><svg width="80" height="14" viewBox="0 0 80 14" fill="#f39a2b"><path id="star" d="M7 0l2 5h5l-4 3 1.6 5L7 10l-4.6 3L4 8 0 5h5z"/><use href="#star" x="16"/><use href="#star" x="32"/><use href="#star" x="48"/><use href="#star" x="64"/></svg></div>
  <p>The team made our first home purchase simple and stress free. They explained every option clearly and found us a great rate fast.</p>
</article>
<article class="abs testi" style="left:460px">
  <svg class="quote" viewBox="0 0 96 96"><path d="M0 0h96v96A96 96 0 0 1 0 0z" fill="#1c5fae"/><text x="52" y="52" fill="#fff" font-family="Poppins,sans-serif" font-size="44" font-weight="700">“</text></svg>
  <div class="avatar" role="img" aria-label="Client portrait"></div>
  <h4>Liam Carter</h4>
  <div class="stars"><svg width="80" height="14" viewBox="0 0 80 14" fill="#f39a2b"><use href="#star"/><use href="#star" x="16"/><use href="#star" x="32"/><use href="#star" x="48"/><use href="#star" x="64"/></svg></div>
  <p>Refinancing through them saved us money every month. Friendly, quick to reply and always honest about what suited us best.</p>
</article>
<article class="abs testi" style="left:780px">
  <svg class="quote" viewBox="0 0 96 96"><path d="M0 0h96v96A96 96 0 0 1 0 0z" fill="#1c5fae"/><text x="52" y="52" fill="#fff" font-family="Poppins,sans-serif" font-size="44" font-weight="700">“</text></svg>
  <div class="avatar" role="img" aria-label="Client portrait"></div>
  <h4>Liam Carter</h4>
  <div class="stars"><svg width="80" height="14" viewBox="0 0 80 14" fill="#f39a2b"><use href="#star"/><use href="#star" x="16"/><use href="#star" x="32"/><use href="#star" x="48"/><use href="#star" x="64"/></svg></div>
  <p>Our equipment finance was sorted within days. Professional service from start to finish, and we would happily recommend them.</p>
</article>

<footer class="abs footer"></footer>
<div class="abs footer-about">
  <div class="brand"><span class="dot"></span>Northvale Finance</div>
  <p>Somos uma empresa de serviços de importação e exportação de cargas para qualquer parte do mundo.</p>
  <div class="social"><span></span><span></span><span></span><span></span></div>
</div>
<div class="abs footer-col footer-links">
  <h4>QUICK LINKS</h4>
  <ul><li>Home</li><li>About</li><li>Services</li><li>Blog</li><li>Contact</li></ul>
</div>
<div class="abs footer-col footer-contact">
  <h4>CONTACT INFO</h4>
  <div class="row"><svg width="20" height="20" viewBox="0 0 24 24" fill="#f39a2b"><path d="M6.6 10.8a15 15 0 0 0 6.6 6.6l2.2-2.2a1 1 0 0 1 1-.25 11.4 11.4 0 0 0 3.6.57 1 1 0 0 1 1 1V20a1 1 0 0 1-1 1A17 17 0 0 1 3 4a1 1 0 0 1 1-1h3.5a1 1 0 0 1 1 1c0 1.25.2 2.45.57 3.57a1 1 0 0 1-.25 1z"/></svg><span>(+61) 2 5550 7731</span></div>
  <div class="row"><svg width="20" height="20" viewBox="0 0 24 24" fill="none" stroke="#f39a2b" stroke-width="2"><rect x="3" y="5" width="18" height="14" rx="2"/><path d="M3 7l9 6 9-6"/></svg><span>hello@northvale.example</span></div>
  <div class="row"><svg width="20" height="20" viewBox="0 0 24 24" fill="#f39a2b"><path d="M12 2a7 7 0 0 0-7 7c0 5 7 13 7 13s7-8 7-13a7 7 0 0 0-7-7zm0 9.5A2.5 2.5 0 1 1 12 6.5a2.5 2.5 0 0 1 0 5z"/></svg><span>18 Wattle St, Parramatta</span></div>
</div>
<div class="abs copyright">Copyright © 2025. All Rights Reserved.</div>

</body>
</html>
```